make it look old timey and motherly but mordern...bath soak with cooling vapors. tall pine hush

need a bath soak label...cooling vapors. will be in a pouch like below. dont pay attention to the design, just attatching so you know the kind of pouch itll be in. need something trusty, minimal and clean...its called tall pine hush bath soak the best bath yull ever take.... for sore muscles, cooling vapors, smells good...made with menthol lemon and eucalyptus...give me something good.

Target Market(s)

make it look old timey and motherly but mordern

Font styles to use
Serif
Sans Serif

Colors
0054AA
0677BA
7BADD7
CADEEF
E8F1F8
0094D4
00A9DD
6FCCEA
C7EBF8
E9F6FB
FFF300
FFF600
FEFA6F
FFFEC7
FFFEE8
FFC000
F8CF3A
FAE287
FDF2CF
FEFAEE
E54698
E96AAD
F1A4CE
F9D9EA
FCEFF6
6B429C
8869AF
B7A5CE
E3DAEB
F3F0F8

```html
<!DOCTYPE html>
<html lang="en">
<head>
<meta charset="utf-8">
<title>Tall Pine Hush Bath Soak – Pouch Label</title>
<link href="https://fonts.googleapis.com/css2?family=Audiowide&family=Play:wght@400;700&family=Roboto+Condensed:ital,wght@0,700;1,700&family=Cabin:wght@400&display=swap" rel="stylesheet">
<style>
  :root {
    --stage: #cbc8c9;
    --pink-deep: #e54698;
    --pink-bright: #f06cb4;
    --pink-mid: #e96aad;
    --pink-soft: #f1a4ce;
    --pink-pale: #f9d9ea;
    --pink-mist: #fceff6;
    --ink-pink: #c0337f;
    --ink-dark: #2a1a24;
    --ink-muted: #a7477c;
    --white: #ffffff;
  }
  * { margin: 0; padding: 0; box-sizing: border-box; }
  html, body { width: 1200px; height: 1000px; overflow: hidden; background: var(--stage); }
  .canvas { position: relative; width: 1200px; height: 1000px; overflow: hidden; background: var(--stage); }
  .shapes { position: absolute; inset: 0; }

  .tagline {
    position: absolute; left: 50px; top: 195px; width: 300px; height: 46px;
    background: var(--white); border-radius: 0 14px 14px 0;
    font: 400 28px/46px "Play", sans-serif; color: var(--ink-pink);
    padding-left: 10px;
  }
  .brand-title {
    position: absolute; text-align: center; color: var(--white);
    font-family: "Audiowide", sans-serif; line-height: 1.1;
    text-shadow: 0 0 2px var(--ink-pink), 0 0 2px var(--ink-pink), 0 2px 3px rgba(150,20,90,.45);
  }
  .brand-title--front { left: 50px; width: 530px; top: 355px; font-size: 44px; }
  .brand-title--back { left: 625px; width: 532px; top: 190px; font-size: 42px; }

  .net-weight {
    position: absolute; width: 300px; text-align: center;
    font: 400 15px/1.35 "Cabin", sans-serif; color: var(--ink-muted);
  }
  .net-weight--front { left: 165px; top: 812px; }
  .net-weight--back { left: 740px; top: 812px; }

  .info-panel {
    position: absolute; left: 700px; top: 287px; width: 386px; height: 494px;
    border: 3px solid var(--pink-deep); border-radius: 30px;
    background: linear-gradient(180deg, rgba(255,255,255,.92), rgba(252,239,246,.92));
    padding: 16px 8px 0 22px;
    font: italic 700 9.2px/1.62 "Roboto Condensed", sans-serif; color: var(--ink-dark);
    letter-spacing: -0.1px;
  }
  .info-panel p { margin-bottom: 12px; }
  .info-panel h3 { font: inherit; }
  .info-panel ul, .info-panel ol { list-style: none; margin-bottom: 12px; }
  .info-panel li { padding-left: 24px; position: relative; white-space: nowrap; }
  .info-panel ul li::before { content: "-"; position: absolute; left: 0; }
  .info-panel ol { counter-reset: step; }
  .info-panel ol li::before { counter-increment: step; content: counter(step) "."; position: absolute; left: 0; }
  .info-panel ol.steps { margin-bottom: 0; }
  .curve-copy { font: 400 22px "Play", sans-serif; fill: var(--ink-pink); }
  .ring-copy { font: 400 22px "Play", sans-serif; fill: var(--ink-pink); }
</style>
</head>
<body>
<main class="canvas">
  <svg class="shapes" width="1200" height="1000" viewBox="0 0 1200 1000">
    <defs>
      <linearGradient id="pouchTop" x1="0" y1="0" x2="0" y2="1">
        <stop offset="0" stop-color="#f0509f"/>
        <stop offset="1" stop-color="#f27cbd"/>
      </linearGradient>
      <linearGradient id="pouchBottom" x1="0" y1="0" x2="0" y2="1">
        <stop offset="0" stop-color="#f6c6df"/>
        <stop offset="1" stop-color="#f2b3d4"/>
      </linearGradient>
      <path id="frontArc" d="M92 505 Q315 690 545 505"/>
      <path id="ringArc" d="M258 748 a62 62 0 1 1 120 -30 a62 62 0 1 1 -120 30"/>
    </defs>

    <g class="pouch pouch--front">
      <rect x="50" y="95" width="530" height="840" rx="14" fill="url(#pouchTop)"/>
      <path d="M50 455 C200 540 410 540 580 440 L580 921 Q580 935 566 935 L64 935 Q50 935 50 921 Z" fill="url(#pouchBottom)"/>
      <path d="M50 425 C200 505 420 505 580 410 L580 428 C420 525 200 525 50 442 Z" fill="var(--pink-deep)"/>
      <path d="M50 442 C200 525 420 525 580 428 L580 444 C420 545 200 545 50 458 Z" fill="#ffffff" opacity=".85"/>
      <line x1="50" y1="148" x2="580" y2="148" stroke="#ffffff" stroke-width="2" stroke-dasharray="8 6"/>
      <circle cx="315" cy="495" r="28" fill="var(--pink-deep)" role="img" aria-label="Flower ornament"/>
      <path d="M248 935 L248 690 L318 632 L386 690 L386 935 Z" fill="#ffffff" opacity=".85"/>
      <circle cx="318" cy="718" r="34" fill="var(--pink-soft)" stroke="var(--pink-deep)" stroke-width="3" role="img" aria-label="Lemon slice illustration"/>
      <text class="ring-copy" textLength="330" lengthAdjust="spacing"><textPath href="#ringArc">menthol  lemon  eucalyptus</textPath></text>
      <text class="curve-copy"><textPath href="#frontArc" startOffset="50%" text-anchor="middle">For sore muscles, cooling vapors, smells good</textPath></text>
      <line x1="235" y1="858" x2="395" y2="858" stroke="var(--ink-muted)" stroke-width="1.5"/>
    </g>

    <g class="pouch pouch--back">
      <rect x="625" y="95" width="532" height="840" rx="14" fill="url(#pouchTop)"/>
      <path d="M625 630 C800 570 1000 510 1157 450 L1157 921 Q1157 935 1143 935 L639 935 Q625 935 625 921 Z" fill="url(#pouchBottom)"/>
      <path d="M625 590 C800 535 1000 470 1157 410 L1157 440 C1000 500 800 565 625 620 Z" fill="var(--pink-deep)"/>
      <path d="M625 620 C800 565 1000 500 1157 440 L1157 456 C1000 516 800 582 625 636 Z" fill="#ffffff" opacity=".85"/>
      <line x1="625" y1="148" x2="1157" y2="148" stroke="#ffffff" stroke-width="2" stroke-dasharray="8 6"/>
      <line x1="810" y1="858" x2="970" y2="858" stroke="var(--ink-muted)" stroke-width="1.5"/>
    </g>
  </svg>

  <div class="tagline">Relax &amp; rejuvenate</div>
  <h1 class="brand-title brand-title--front">Tall Pine Hush<br>Bath Soak</h1>
  <p class="net-weight net-weight--front">Net Weigth<br>10 Ounces 283,5 grams</p>

  <h2 class="brand-title brand-title--back">Tall Pine Hush<br>Bath Soak</h2>
  <section class="info-panel">
    <p>The Best Bath You'll Ever Take...</p>
    <p>Discover the ultimate relaxation with Tall Pine Hush Bath Soak,<br>expertly crafted to provide a rejuvenating experience for both body and mind.</p>
    <h3>Benefits:</h3>
    <ul>
      <li>Soothes Sore Muscles</li>
      <li>Invigorating Cooling Vapors</li>
      <li>Irresistible Fragrance</li>
    </ul>
    <h3>Key Ingredients:</h3>
    <ul>
      <li>Menthol: Known for its cooling properties, promoting a refreshing sensation.</li>
      <li>Lemon: Infused for a burst of invigorating citrus goodness.</li>
      <li>Eucalyptus: Renowned for its aromatic essence, enhancing the overall bath experience.</li>
    </ul>
    <h3>Directions for Use:</h3>
    <ol class="steps">
      <li>Fill your tub with warm water.</li>
      <li>Add desired amount of Tall Pine Hush Bath Soak.</li>
      <li>Immerse yourself and let the cooling vapors envelop you.</li>
      <li>Breathe deeply and relax.</li>
    </ol>
    <h3>Caution:</h3>
    <p>For external use only. Avoid contact with eyes.<br>Keep out of reach of children. If irritation occurs, discontinue use.</p>
    <h3>Storage:</h3>
    <p>Store in a cool, dry place.</p>
    <h3>Ingredients:</h3>
    <p>Sodium Bicarbonate, Citric Acid, Menthol, Lemon Extract, Eucalyptus Oil, and love.<br>Made for the calm in you, because every soak should feel like home.</p>
  </section>
  <p class="net-weight net-weight--back">Net Weigth<br>10 Ounces 283,5 grams</p>
</main>
</body>
</html>
```